Complete collections of detective novels by Damien Valtrenoux

Cover for a NUMERIC book: all the 11 detective novels by Damien Valtrenoux.
Covers of these novels can be seen at https://www.editions-brunelle.example/auteur/damien-valtrenoux/ (but we don't want a patchwork).
All these books are connected with a medical atmosphere, they often include a beautiful women, some bandits and a detective.

Title: “The Cases of Dr. V – The Complete 2024”
Author: “Damien Valtrenoux”
Publisher: “Editions Brunelle”

Target Market(s)

Readers of detective novels

Requirements
Must have
• Adapted to screen (it's a digital book)

```html
<!DOCTYPE html>
<html lang="en">
<head>
<meta charset="utf-8">
<title>The Cases of Dr. V – The Complete 2024</title>
<link rel="stylesheet" href="https://fonts.googleapis.com/css2?family=Oswald:wght@400&family=Michroma&display=swap">
<style>
  :root {
    --backdrop: #555555;
    --navy-deep: #0b1636;
    --navy: #1d3566;
    --steel: #4f6c9e;
    --haze: #c9d6ea;
    --light: #ffffff;
    --ink: #0a0a0a;
    --subtitle: #0f1f4a;
  }
  html, body {
    margin: 0;
    width: 1200px;
    height: 1200px;
    overflow: hidden;
    background: var(--backdrop);
  }
  .cover {
    position: absolute;
    left: 229px;
    top: 43px;
    width: 742px;
    height: 1113px;
    overflow: hidden;
  }
  .cover-art {
    position: absolute;
    inset: 0;
    background:
      radial-gradient(ellipse 46% 42% at 50% 50%, var(--light) 0%, rgba(255,255,255,0.92) 30%, rgba(201,214,234,0.55) 60%, rgba(201,214,234,0) 85%),
      radial-gradient(ellipse 80% 70% at 50% 48%, var(--steel) 0%, var(--navy) 60%, var(--navy-deep) 100%);
  }
  .title-line {
    position: absolute;
    left: 0;
    width: 100%;
    margin: 0;
    text-align: center;
    font-family: "Oswald", sans-serif;
    font-weight: 400;
    color: var(--ink);
    line-height: 1;
    transform: scaleX(0.78);
    text-shadow: 0 0 6px rgba(255,255,255,0.9), 0 0 18px rgba(255,255,255,0.8);
  }
  .title-the    { top: 225px; font-size: 146px; }
  .title-cases  { top: 355px; font-size: 146px; }
  .title-of     { top: 488px; font-size: 146px; }
  .title-doctor { top: 604px; font-size: 202px; }
  .subtitle, .author, .publisher {
    position: absolute;
    left: 0;
    width: 100%;
    margin: 0;
    text-align: center;
    font-family: "Michroma", sans-serif;
    line-height: 1;
  }
  .subtitle {
    top: 813px;
    font-size: 19px;
    letter-spacing: 0.42em;
    color: var(--subtitle);
  }
  .author {
    top: 983px;
    font-size: 22px;
    letter-spacing: 0.28em;
    color: var(--light);
  }
  .publisher {
    top: 1033px;
    font-size: 12px;
    letter-spacing: 0.45em;
    color: var(--navy-deep);
  }
</style>
</head>
<body>
  <main class="cover">
    <div class="cover-art" role="img" aria-label="Photograph of a hospital corridor flooded with bright light, a lone silhouetted figure standing in the glow"></div>
    <h1 class="title">
      <span class="title-line title-the">THE</span>
      <span class="title-line title-cases">CASES</span>
      <span class="title-line title-of">OF</span>
      <span class="title-line title-doctor">DR. V</span>
    </h1>
    <p class="subtitle">THE COMPLETE 2024</p>
    <p class="author">DAMIEN VALTRENOUX</p>
    <p class="publisher">EDITIONS BRUNELLE</p>
  </main>
</body>
</html>
```